K7R Business Cards

Business Cards

Contact Information for Business Card

Company name, owner name, license #s, phone & email

Requirements
Should not have
• mailing address

```html
<!DOCTYPE html>
<html lang="en">
<head>
<meta charset="utf-8">
<title>K7R Construction Business Cards</title>
<link href="https://fonts.googleapis.com/css2?family=Montserrat:wght@400;500;800&display=swap" rel="stylesheet">
<style>
  :root {
    --navy: #0f2d6e;
    --navy-deep: #0a2460;
    --red: #d81c1c;
    --white: #ffffff;
    --ink: #1d1d1f;
    --backdrop: #3a3a3c;
    --photo-light: #e9e9ea;
    --photo-dark: #2b2b30;
  }
  * { box-sizing: border-box; margin: 0; padding: 0; }
  html, body { width: 1200px; height: 1200px; overflow: hidden; }
  body {
    background: var(--backdrop);
    font-family: "Montserrat", Arial, sans-serif;
    position: relative;
  }
  .card {
    position: absolute;
    left: 250px;
    width: 700px;
    height: 400px;
    border-radius: 34px;
    overflow: hidden;
    box-shadow: 0 14px 30px rgba(0,0,0,.45);
  }
  .card-front { top: 150px; background: var(--white); }
  .card-back {
    top: 640px;
    background: linear-gradient(135deg, #0c2a68 0%, var(--navy-deep) 55%, #08215a 100%);
    display: flex; align-items: center; justify-content: center;
  }

  .brand-front {
    position: absolute; left: 60px; top: 70px;
    color: var(--navy); font-weight: 800; line-height: .9;
  }
  .brand-front .brand-name { font-size: 92px; letter-spacing: 2px; display: block; }
  .brand-front .brand-sub { font-size: 27px; letter-spacing: 1px; display: block; margin-top: 6px; }

  .contact-list {
    position: absolute; left: 64px; top: 230px;
    list-style: none; color: var(--ink);
    font-size: 19px; font-weight: 500; line-height: 1.25;
  }
  .contact-list li { display: flex; align-items: flex-start; gap: 12px; margin-bottom: 8px; }
  .contact-list svg { width: 20px; height: 20px; flex: none; margin-top: 2px; fill: var(--red); }
  .contact-list .license { padding-left: 32px; font-size: 16px; margin-top: 6px; letter-spacing: .5px; }

  .portrait {
    position: absolute; right: 120px; top: 50px;
    width: 180px; height: 180px; border-radius: 50%;
    border: 3px solid var(--navy);
    background: linear-gradient(180deg, var(--photo-light) 0%, var(--photo-light) 55%, var(--photo-dark) 100%);
  }
  .owner-name {
    position: absolute; right: 60px; top: 250px;
    color: var(--navy); font-size: 30px; font-weight: 400; letter-spacing: 1px;
  }
  .card-stripe { position: absolute; left: 0; bottom: 0; width: 700px; height: 80px; }

  .brand-back { color: var(--white); font-weight: 800; text-align: center; line-height: .9; }
  .brand-back .brand-name { font-size: 160px; letter-spacing: 4px; display: block; }
  .brand-back .brand-sub { font-size: 46px; letter-spacing: 2px; display: block; margin-top: 10px; }
</style>
</head>
<body>
  <section class="card card-front">
    <div class="brand-front">
      <span class="brand-name">K7R</span>
      <span class="brand-sub">CONSTRUCTION</span>
    </div>

    <ul class="contact-list">
      <li>
        <svg viewBox="0 0 24 24"><path d="M6.6 10.8a15.1 15.1 0 0 0 6.6 6.6l2.2-2.2c.3-.3.7-.4 1-.2 1.1.4 2.3.6 3.6.6.6 0 1 .4 1 1V20c0 .6-.4 1-1 1A17 17 0 0 1 3 4c0-.6.4-1 1-1h3.5c.6 0 1 .4 1 1 0 1.3.2 2.5.6 3.6.1.3 0 .7-.2 1z"/></svg>
        <span>555-014-2290</span>
      </li>
      <li>
        <svg viewBox="0 0 24 24"><path d="M2 5h20v14H2z" fill="none" stroke="#d81c1c" stroke-width="2"/><path d="M2 5l10 8 10-8" fill="none" stroke="#d81c1c" stroke-width="2"/></svg>
        <span>dwhitfield@k7rbuild.com</span>
      </li>
      <li class="license">MN LICENSE #BC482715</li>
    </ul>

    <div class="portrait" role="img" aria-label="Portrait photo of the owner in a dark suit"></div>
    <div class="owner-name">DANA WHITFIELD</div>

    <svg class="card-stripe" viewBox="0 0 700 80" preserveAspectRatio="none" aria-hidden="true">
      <polygon points="0,62 440,46 440,80 0,80" fill="var(--red)"/>
      <polygon points="448,46 700,30 700,80 448,80" fill="var(--navy)"/>
    </svg>
  </section>

  <section class="card card-back">
    <div class="brand-back">
      <span class="brand-name">K7R</span>
      <span class="brand-sub">CONSTRUCTION</span>
    </div>
  </section>
</body>
</html>
```